Buch-/E-Book-Cover im Bereich der Persönlichkeitsentwicklung
Vielen lieben Dank für die super Arbeit von Dir. Das Design ist klasse und die vielen Vorschläge waren auch super. Die komplette Zusammenarbeit verlief sehr professionell und Änderungswünsche wurden sehr schnell umgesetzt. Ich kann Dich voll und ganz weiterempfehlen.
Zielgruppe
Wir arbeiten in der Persönlichkeitsentwicklung für Jugendliche. Dabei spezialisieren wir uns auf den Altersbereich 12 - 17 Jahre. Unser Ziel ist es jungen Menschen zu zeigen, wie Sie zu sich selbst finden und ein glückliches sowie erfolgreiches Leben führen können.
Aufgabenstellung
- Das Design sollte für die Eltern von Teenagern und auch für die Teenager selbst ausgelegt werden. Das Buch ist für die Jugendlichen (Mädchen und Jungen im Alter zwischen 12 Jahren und 17 Jahren) gedacht, wird allerdings meist von deren Mütter gekauft.
- Der Name des Autors lautet: Jochen Brabeck
- Der Titel lautet: Junge Leute finden Mut und Richtung
- Der Untertitel lautet: Was Heranwachsende über eigene Stärken lernen
- Im Anhang befinden sich Designs, die ich gut finde (nur falls jemand weitere Ideen haben möchte)
- Format: 15,24 cm x 22,86 cm (6' x 9') [genaue Maße fürs Taschenbuch und Hardcover sind im Anhang (.zip Dateien)]
1. E-Book:
- Coverdateien sollten idealerweise 2 560 Pixel hoch und 1 600 Pixel breit sein. Zur Gewährleistung der bestmöglichen Qualität (insbesondere auf HD-Geräten) sollte das Bild mindestens 2 500 Pixel hoch sein.
- Format: TIFF (.tif/.tiff) oder JPEG (.jpeg/.jpg)
- DPI: 72 dpi
- Größe: Ihr Coverbild muss kleiner als 50 MB sein.
Hinweis: Vermeiden Sie es, Ihre Dateien zu komprimieren. Dies kann die Qualität Ihres Covers auf Lesegeräten beeinträchtigen. Das beste Ergebnis erzielen Sie mit Bildern, die eine Mindestauflösung von 300 ppi (Pixels per Inch) haben.
- Rahmen: Coverbilder mit weißem oder sehr hellem Hintergrund heben sich kaum vom weißen Hintergrund ab. Fügen Sie einen dünnen Rahmen (3–4 Pixel) in Mittelgrau hinzu, um die Ränder des Covers besser sichtbar zu machen.
2. + 3. Taschenbuch/Hardcover [genaue Maße fürs Taschenbuch und Hardcover sind im Anhang (.zip Dateien)] :
- Dateityp: Das Cover muss als einzelne PDF-Datei vorliegen und die hintere Coverseite, den Buchrücken und die vordere Coverseite als einzelnes Bild enthalten.
- Dateigröße: Coverdateien, die größer als 650 MB sind, können nicht konvertiert werden. Die Datei sollte maximal 40 MB groß sein, da sich bei großen Dateien der Druck verlangsamt.
- Die gen..

```html
<!DOCTYPE html>
<html lang="de">
<head>
<meta charset="utf-8">
<title>Junge Leute finden Mut und Richtung – Buchcover</title>
<link rel="stylesheet" href="https://fonts.googleapis.com/css2?family=Londrina+Solid:wght@300;900&family=Roboto+Condensed:wght@700&family=Amatic+SC:wght@700&display=swap">
<style>
  :root {
    --page: #ffffff;
    --sky-top: #c3dcf2;
    --sky-bottom: #d9ebf8;
    --title-grey: #6f6655;
    --title-orange: #e36c14;
    --ink: #1c1c1c;
    --rock-light: #8a8275;
    --rock-dark: #4a443c;
    --edge: #555555;
  }
  html, body {
    margin: 0;
    width: 1200px;
    height: 1200px;
    overflow: hidden;
    background: var(--page);
  }
  .cover {
    position: absolute;
    left: 234px;
    top: 47px;
    width: 695px;
    height: 1117px;
    border: 1px solid var(--edge);
    box-sizing: border-box;
    overflow: hidden;
    background: linear-gradient(180deg, var(--sky-top) 0%, var(--sky-bottom) 70%, #e2eff9 100%);
  }
  .author {
    position: absolute;
    top: 46px;
    left: 0;
    width: 100%;
    text-align: center;
    font: 700 30px/1 "Roboto Condensed", sans-serif;
    letter-spacing: 1.5px;
    color: var(--ink);
    text-transform: uppercase;
    margin: 0;
  }
  .title { margin: 0; font-weight: normal; }
  .title span { position: absolute; white-space: nowrap; line-height: 1; }
  .title .big {
    font-family: "Londrina Solid", sans-serif;
    font-weight: 900;
  }
  .title .small {
    font-family: "Londrina Solid", sans-serif;
    font-weight: 300;
    color: var(--title-grey);
  }
  .line-1 { top: 128px; left: 0; width: 100%; text-align: center; font-size: 118px; color: var(--title-grey); }
  .line-2 { top: 280px; left: 265px; font-size: 54px; }
  .line-3 { top: 330px; left: 68px; font-size: 176px; color: var(--title-orange); }
  .line-3b { top: 440px; left: 390px; font-size: 54px; }
  .line-4 { top: 492px; right: 38px; font-size: 124px; color: var(--title-orange); }
  .subtitle {
    position: absolute;
    top: 640px;
    right: 300px;
    margin: 0;
    text-align: right;
    font: 700 34px/1.25 "Amatic SC", sans-serif;
    color: var(--ink);
    letter-spacing: 1px;
  }
  .photo {
    position: absolute;
    left: 0;
    right: 0;
    bottom: 0;
    height: 420px;
    background:
      linear-gradient(180deg, rgba(138,130,117,0) 0%, rgba(138,130,117,0) 45%, var(--rock-light) 62%, var(--rock-dark) 100%);
  }
</style>
</head>
<body>
  <main class="cover">
    <div class="photo" role="img" aria-label="Foto: vier Jugendliche sitzen im Sommerlicht auf einer alten Steinmauer vor blauem Himmel"></div>
    <p class="author">Jochen Brabeck</p>
    <h1 class="title">
      <span class="big line-1">Junge Leute</span>
      <span class="small line-2">finden</span>
      <span class="big line-3">Mut</span>
      <span class="small line-3b">und</span>
      <span class="big line-4">Richtung</span>
    </h1>
    <p class="subtitle">Was Heranwachsende<br>über eigene<br>Stärken lernen</p>
  </main>
</body>
</html>
```